New Business Card Design Project

I need a design for business cards, i am an electrical business called "Kelvora Electrical and Communications" i need the cards to be double sided with the company logo on the back (attached) the front needs to say my company name, web site, email address, telephone number, and ABN number and electrical license number. I am open to different arrangements of the information but would like the background to be incorporating something electrical or something that looks smart. open to all additional ideas also.

The company colours are orange and grey see logo attached.

Business Name: Kelvora Electrical and Communications
Website: kelvoraelectricalandcomms.example.au
Email: dean@kelvoraelectricalandcomms.example.au
Telephone(mobile): 0481290736
ABN: 71829304516
Lic No: 483027D

Target Market(s)

Business entities, Project Managers, Accounts, Clients

Industry/Entity Type

Electrician

Contact Information for Business Card

I need a design for business cards, i am an electrical business called "Kelvora Electrical and Communications" i need the cards to be double sided with the company logo on the back (attached) the front needs to say my company name

Font styles to use
Serif
Sans Serif

Colors
f37122
5c5c5c

Requirements
Must have
• Must have the Logo on the back open to different ways of it being on the back but had in mind to keep it central but again open to other options
Nice to have
• A real modern cool background that is eye catching yet contemporary
Should not have
• No backgrounds of a light bulb or plug or anything like that

```html
<!DOCTYPE html>
<html lang="en">
<head>
<meta charset="utf-8">
<title>Kelvora Electrical and Communications – Business Cards</title>
<link rel="stylesheet" href="https://fonts.googleapis.com/css2?family=Exo+2:wght@500;600;700&display=swap">
<style>
  :root {
    --stage: #1c1c1c;
    --grey: #58585a;
    --grey-dark: #3a3a3c;
    --orange: #f8a81f;
    --white: #ffffff;
    --font: "Exo 2", sans-serif;
  }
  * { box-sizing: border-box; margin: 0; padding: 0; }
  html, body { width: 1200px; height: 800px; overflow: hidden; }
  body {
    background: var(--stage);
    font-family: var(--font);
    position: relative;
  }
  .card {
    position: absolute;
    top: 246px;
    width: 540px;
    height: 308px;
    background: var(--grey);
    overflow: hidden;
    box-shadow: 0 10px 30px rgba(0,0,0,.5);
  }
  .card--back { left: 40px; }
  .card--front { left: 620px; }

  /* back side */
  .back__rule-top {
    position: absolute; left: 0; right: 0; top: 30px;
    height: 3px; background: var(--orange);
  }
  .back__rule-low {
    position: absolute; left: 0; right: 0; top: 228px;
    height: 2px; background: var(--orange);
  }
  .back__band {
    position: absolute; left: 0; right: 0; top: 238px; height: 30px;
    background: var(--orange);
    display: flex; align-items: center; padding-left: 60px;
  }
  .back__url {
    color: var(--white); font-weight: 600; font-size: 15px; letter-spacing: .2px;
    white-space: nowrap;
  }
  .back__rule-white {
    position: absolute; left: 0; right: 0; top: 274px;
    height: 3px; background: var(--white);
  }
  .brand {
    position: absolute;
    display: flex; align-items: center; gap: 12px;
  }
  .brand__dot {
    width: 16px; height: 16px; border-radius: 50%; background: var(--orange);
    flex: none;
  }
  .brand__name {
    color: var(--white); font-weight: 600; letter-spacing: 3px;
    text-transform: uppercase; line-height: 1; white-space: nowrap;
  }
  .card--back .brand { left: 110px; top: 104px; }
  .card--back .brand__name { font-size: 58px; }

  /* front side */
  .front__rule-top {
    position: absolute; left: 0; right: 0; top: 56px;
    height: 4px; background: var(--white);
  }
  .front__band {
    position: absolute; left: 0; right: 0; top: 66px; height: 160px;
    background: var(--orange);
  }
  .card--front .brand { right: 38px; top: 22px; }
  .card--front .brand__name { font-size: 40px; }
  .card--front .brand__dot { background: var(--white); }
  .contact {
    position: absolute; left: 0; right: 0; top: 88px;
    text-align: center; color: var(--grey-dark);
    font-weight: 700; font-size: 15px; line-height: 1.45;
    white-space: nowrap;
  }
  .front__rule-low {
    position: absolute; left: 0; right: 0; top: 232px;
    height: 4px; background: var(--white);
  }
  .registration {
    position: absolute; left: 0; right: 0; top: 246px;
    text-align: center; color: var(--white);
    font-weight: 600; font-size: 14px; letter-spacing: .3px;
  }
  .registration span + span { margin-left: 14px; }
</style>
</head>
<body>
  <section class="card card--back" aria-label="Business card back">
    <div class="back__rule-top"></div>
    <div class="brand">
      <span class="brand__dot"></span>
      <span class="brand__name">Kelvora</span>
    </div>
    <div class="back__rule-low"></div>
    <div class="back__band">
      <span class="back__url">www.kelvoraelectricalandcomms.example.au</span>
    </div>
    <div class="back__rule-white"></div>
  </section>

  <section class="card card--front" aria-label="Business card front">
    <div class="front__rule-top"></div>
    <div class="front__band">
      <div class="brand">
        <span class="brand__dot"></span>
        <span class="brand__name">Kelvora</span>
      </div>
      <div class="contact">
        <p>Mobile: 0481290736</p>
        <p>Web: kelvoraelectricalandcomms.example.au</p>
        <p>Email: dean@kelvoraelectricalandcomms.example.au</p>
      </div>
    </div>
    <div class="front__rule-low"></div>
    <p class="registration"><span>ABN: 71829304516</span><span>LIC NO: 483027D</span></p>
  </section>
</body>
</html>
```